Creative, Striking, Responsive Tutoring Flyer

I need a designer superstar to create an attractive, modern and eye-catching flyer for me. I'm a teacher and I need the flyer to sell French & German private lessons.

Attached is an example that I like a lot. Please create a similar design.

```html
<!DOCTYPE html>
<html lang="en">
<head>
<meta charset="utf-8">
<title>French &amp; German Private Lessons Flyer</title>
<link rel="stylesheet" href="https://fonts.googleapis.com/css2?family=Alfa+Slab+One&family=Roboto+Slab:wght@400;500;700&family=Roboto:wght@700&display=swap">
<style>
  :root {
    --page-bg: #c4c4c4;
    --board-light: #474d53;
    --board-dark: #25292d;
    --chalk-white: #f2f2f2;
    --chalk-yellow: #f4f01c;
    --ribbon-yellow: #ffff00;
    --ink-dark: #2e3338;
    --text-white: #ffffff;
  }
  html, body {
    margin: 0;
    width: 1200px;
    height: 1200px;
    overflow: hidden;
    background: var(--page-bg);
  }
  .flyer {
    position: absolute;
    left: 180px;
    top: 57px;
    width: 840px;
    height: 1086px;
    overflow: hidden;
    background: radial-gradient(ellipse at 55% 25%, var(--board-light) 0%, #363b40 45%, var(--board-dark) 100%);
  }
  .headline {
    position: absolute;
    left: 0;
    top: 0;
    width: 840px;
    height: 340px;
  }
  .headline .chalk { font-family: "Alfa Slab One", serif; fill: var(--chalk-white); }
  .headline .chalk-yellow { font-family: "Alfa Slab One", serif; fill: var(--chalk-yellow); }
  .ribbon {
    position: absolute;
    left: 0;
    top: 370px;
    width: 840px;
    height: 150px;
  }
  .tutor-name {
    position: absolute;
    left: 191px;
    width: 450px;
    top: 410px;
    margin: 0;
    text-align: center;
    font-family: "Roboto Slab", serif;
    font-weight: 500;
    font-size: 48px;
    line-height: 52px;
    letter-spacing: -1px;
    color: var(--ink-dark);
  }
  .tutor-role, .contact-phone, .contact-email, .contact-social {
    position: absolute;
    left: 0;
    width: 840px;
    margin: 0;
    text-align: center;
    color: var(--text-white);
  }
  .tutor-role {
    top: 502px;
    font-family: "Roboto Slab", serif;
    font-weight: 700;
    font-size: 30px;
    line-height: 36px;
    padding-left: 0;
    left: 0;
    width: 836px;
  }
  .contact-phone {
    top: 552px;
    font-family: "Roboto", sans-serif;
    font-weight: 700;
    font-size: 62px;
    line-height: 66px;
    width: 838px;
  }
  .contact-email {
    top: 620px;
    font-family: "Roboto Slab", serif;
    font-weight: 500;
    font-size: 40px;
    line-height: 48px;
    width: 842px;
  }
  .contact-social {
    top: 690px;
    font-family: "Roboto Slab", serif;
    font-weight: 400;
    font-size: 26px;
    line-height: 30px;
    display: flex;
    justify-content: center;
    align-items: center;
    gap: 14px;
    width: 870px;
  }
  .contact-social .dot {
    width: 24px;
    height: 24px;
    border-radius: 50%;
    background: var(--text-white);
  }
  .supplies-art {
    position: absolute;
    left: 0;
    top: 730px;
    width: 840px;
    height: 356px;
    background:
      linear-gradient(to bottom, rgba(37,41,45,0) 0%, rgba(37,41,45,0) 20%, rgba(37,41,45,0.0) 100%),
      linear-gradient(100deg, #6fae2e 0%, #e9e9e9 18%, #f5a623 35%, #e0407a 50%, #2f6fd6 62%, #38b6e8 75%, #f3c23a 85%, #c9ccd0 100%);
    -webkit-mask-image: linear-gradient(to bottom, transparent 0%, rgba(0,0,0,0.6) 30%, #000 65%);
    mask-image: linear-gradient(to bottom, transparent 0%, rgba(0,0,0,0.6) 30%, #000 65%);
  }
</style>
</head>
<body>
  <main class="flyer">
    <svg class="headline" viewBox="0 0 840 340" aria-label="French and German private lessons">
      <text class="chalk" x="96" y="128" font-size="110" textLength="650" lengthAdjust="spacingAndGlyphs">FRENCH &amp;</text>
      <text class="chalk" x="109" y="246" font-size="120" textLength="622" lengthAdjust="spacingAndGlyphs">GERMAN</text>
      <text class="chalk-yellow" x="96" y="325" font-size="64" textLength="650" lengthAdjust="spacingAndGlyphs">PRIVATE LESSONS</text>
    </svg>

    <svg class="ribbon" viewBox="0 370 840 150" aria-hidden="true">
      <polygon fill="var(--ribbon-yellow)" points="96,409 183,409 177,509 85,509 145,459"/>
      <polygon fill="var(--ribbon-yellow)" points="644,409 733,409 683,459 721,509 632,509"/>
      <polygon fill="var(--ribbon-yellow)" points="193,383 642,383 636,483 188,483"/>
    </svg>

    <h2 class="tutor-name">MARTIN HALE</h2>
    <p class="tutor-role">OUR PERSONAL TRAINER</p>
    <p class="contact-phone">800-555-0142</p>
    <p class="contact-email">lessons@halelingua.com</p>
    <p class="contact-social"><span class="dot"></span><span>@halelingua.lessons</span></p>

    <div class="supplies-art" role="img" aria-label="School supplies spread across the chalkboard: green apple, notebook, scissors, markers, coloured pencils, paperclips, push pins, ruler and calculator"></div>
  </main>
</body>
</html>
```